New Infographic Design Project

I need a 1 page Infographic that explains our Quillstone Prism offer.

Can you use the following content in the attached document to create a 1 page infographic. The image in the bottom of the document is one of our competitors who is offering the same thing, this image is only provided for inspiration and ideas as we need ours to be based on the content of the document and aligned with the Corvenly Brand

```html
<!DOCTYPE html>
<html lang="en">
<head>
<meta charset="utf-8">
<title>Quillstone Prism – Data Ready, AI Ready in 6 Weeks</title>
<link rel="stylesheet" href="https://fonts.googleapis.com/css2?family=Bebas+Neue&family=Barlow:ital,wght@1,700&family=Inter:wght@400;600&display=swap">
<style>
:root{
  --ink:#000;
  --white:#fff;
  --sky:#7fd0f5;
  --blue-line:#2a8fd6;
  --navy:#17184a;
  --cyan:#2aaee6;
  --azure:#1479c4;
  --indigo:#2e3a9a;
  --violet:#2b2878;
}
*{margin:0;padding:0;box-sizing:border-box}
html,body{width:1200px;height:848px;overflow:hidden;background:var(--ink)}
.sheet{position:relative;width:1200px;height:848px;background:var(--ink);color:var(--white);font-family:"Inter",sans-serif;overflow:hidden}
.abs{position:absolute}
.display{font-family:"Bebas Neue",sans-serif;font-weight:400;text-transform:uppercase;white-space:nowrap}

.hero-title{left:62px;top:40px;font-size:88px;line-height:69px;letter-spacing:-1px;transform:skewX(-9deg);transform-origin:bottom left;
  background:linear-gradient(180deg,#9fdcf7 0%,#3aa7dc 55%,#2483c2 100%);-webkit-background-clip:text;background-clip:text;color:transparent}
.quote-mark{left:414px;top:53px}
.partner-title{left:592px;top:50px;font-size:64px;line-height:54px;letter-spacing:-.3px}
.intro{left:414px;top:177px;width:730px;font-size:13.4px;line-height:18.6px}

.section-rule{top:292px;height:2px;background:var(--blue-line)}
.section-title{text-align:center}
.edge-title{left:446px;top:268px;width:300px;font-size:50px;line-height:50px}
.value-title{left:396px;top:446px;width:410px;font-size:52px;line-height:52px}

.edge{top:332px}
.edge-head{display:flex;align-items:center;gap:8px;height:40px}
.edge-name{font-family:"Barlow",sans-serif;font-style:italic;font-weight:700;font-size:16.5px;line-height:17px}
.edge-text{margin-top:5px;font-size:13.5px;line-height:17px}

.timeline{left:55px;top:555px;width:1082px;height:2px;background:var(--blue-line)}
.dot{top:550px;width:11px;height:11px;border-radius:50%;background:var(--blue-line)}
.week{top:516px;width:160px}
.week-label{font-size:30px;line-height:30px;letter-spacing:-.3px}
.week-name{margin-top:24px;font-family:"Barlow",sans-serif;font-style:italic;font-weight:700;font-size:15.5px;line-height:16px;white-space:nowrap}
.week-text{margin-top:8px;font-size:12px;line-height:14.3px}

.extra-band{left:0;top:708px}
.extra-title{left:48px;top:726px;font-size:58px;line-height:52px;transform:skewX(-9deg)}
.extra-title span{display:block;padding-left:28px}
.extra-item{top:736px;width:215px}
.extra-name{font-weight:600;font-size:15px;line-height:18px}
.extra-text{margin-top:4px;font-size:12.3px;line-height:15.5px}
</style>
</head>
<body>
<main class="sheet">

  <h1 class="abs display hero-title">Data Ready.<br>AI Ready.<br>In 6 Weeks.</h1>

  <svg class="abs quote-mark" width="132" height="102" viewBox="0 0 132 104" aria-hidden="true">
    <path fill="#7fd0f5" d="M24 0h20L36 56h16v48H0V56h12z"/>
    <path fill="#7fd0f5" d="M104 0h20L116 56h16v48H80V56h12z"/>
  </svg>

  <h2 class="abs display partner-title">Your long-term<br>strategic data partner</h2>

  <p class="abs intro">We start with a Business Data Assessment or Prism Deployment Assessment to pinpoint the highest-value use cases, the biggest data risks, and the fastest path to impact. We stand up a governed Quillstone Prism foundation using repeatable ingestion, validation, and common data model patterns, so your reporting scales cleanly and your AI initiatives provide business value.</p>

  <div class="abs section-rule" style="left:55px;width:400px"></div>
  <div class="abs section-rule" style="left:735px;width:401px"></div>
  <h2 class="abs display section-title edge-title">The Corvenly Edge</h2>

  <section class="abs edge" style="left:62px;width:230px">
    <div class="edge-head">
      <svg width="38" height="40" viewBox="0 0 38 40" aria-hidden="true">
        <path fill="#7fd0f5" d="M8 24l-5 12 7-2 4 6 5-12zM30 24l5 12-7-2-4 6-5-12z"/>
        <circle cx="19" cy="16" r="15" fill="#7fd0f5"/>
        <circle cx="19" cy="16" r="10" fill="none" stroke="#000" stroke-width="2.5"/>
      </svg>
      <div class="edge-name">Quality-first<br>Delivery</div>
    </div>
    <p class="edge-text">Automated validation, data tests, and “quality gates” that stop bad data upstream.</p>
  </section>

  <section class="abs edge" style="left:350px;width:270px">
    <div class="edge-head">
      <svg width="42" height="36" viewBox="0 0 42 36" aria-hidden="true">
        <path fill="#7fd0f5" d="M21 2l19 9-19 9-19-9z"/>
        <path fill="none" stroke="#7fd0f5" stroke-width="3.5" d="M3 18l18 9 18-9M3 25l18 9 18-9"/>
      </svg>
      <div class="edge-name">Data Products,<br>Not Datasets</div>
    </div>
    <p class="edge-text">Clear ownership, SLAs, versioning, and reusable, consumable outputs aligned to high impact business outcomes.</p>
  </section>

  <section class="abs edge" style="left:663px;width:260px">
    <div class="edge-head">
      <svg width="38" height="38" viewBox="0 0 38 38" aria-hidden="true">
        <rect x="1" y="15" width="8" height="21" rx="1.5" fill="#7fd0f5"/>
        <path fill="#7fd0f5" d="M12 15l7-12c3-1 5 1 4.5 4L22 14h11c3 0 4.5 3 3.5 5l-4 14c-.8 2-2.3 3-4.5 3H12z"/>
      </svg>
      <div class="edge-name">Governance That<br>Doesn’t Slow You Down</div>
    </div>
    <p class="edge-text">Security, access, lineage, and auditability built in from day one.</p>
  </section>

  <section class="abs edge" style="left:938px;width:210px">
    <div class="edge-head">
      <svg width="36" height="36" viewBox="0 0 36 36" aria-hidden="true">
        <g fill="#7fd0f5" transform="translate(18 18)">
          <rect x="-4" y="-18" width="8" height="36" rx="1.5"/>
          <rect x="-4" y="-18" width="8" height="36" rx="1.5" transform="rotate(45)"/>
          <rect x="-4" y="-18" width="8" height="36" rx="1.5" transform="rotate(90)"/>
          <rect x="-4" y="-18" width="8" height="36" rx="1.5" transform="rotate(135)"/>
          <circle r="13"/>
        </g>
        <circle cx="18" cy="18" r="6" fill="#000"/>
      </svg>
      <div class="edge-name">Operate<br>Seamlessly</div>
    </div>
    <p class="edge-text">CI/CD, monitoring, and cost controls so the platform stays healthy.</p>
  </section>

  <h2 class="abs display section-title value-title">6 Week Time to Value</h2>

  <div class="abs timeline"></div>
  <div class="abs dot" style="left:50px"></div>
  <div class="abs dot" style="left:213px"></div>
  <div class="abs dot" style="left:399px"></div>
  <div class="abs dot" style="left:582px"></div>
  <div class="abs dot" style="left:765px"></div>
  <div class="abs dot" style="left:947px"></div>
  <div class="abs dot" style="left:1131px"></div>

  <section class="abs week" style="left:53px">
    <div class="week-label display">Week 1</div>
    <div class="week-name">Envision<br>&amp; Assess</div>
    <p class="week-text">Use case shortlist and priority based on highest business impact, current-state review, data risk &amp; compliance priorities, target operating model.</p>
  </section>
  <section class="abs week" style="left:235px">
    <div class="week-label display">Week 2</div>
    <div class="week-name">Architecture &amp;<br>governance design</div>
    <p class="week-text">Landing zone decisions, security and access model, patterns/ standards, delivery plan and success metrics.</p>
  </section>
  <section class="abs week" style="left:417px">
    <div class="week-label display">Week 3</div>
    <div class="week-name">Prism foundation<br>deployed</div>
    <p class="week-text">Workspaces and environments, automation &amp; CI/CD, onboarding playbooks, baseline policies/guardrails.</p>
  </section>
  <section class="abs week" style="left:599px">
    <div class="week-label display">Week 4</div>
    <div class="week-name">Data ingestion +<br>validation framework</div>
    <p class="week-text">Reusable ingestion patterns, automated validation, data contracts/SLAs, observability signals and alerting.</p>
  </section>
  <section class="abs week" style="left:781px">
    <div class="week-label display">Week 5</div>
    <div class="week-name">Scalable common<br>data model</div>
    <p class="week-text">Domain model, master entities, curated layer, semantic modelling patterns that support Lumetric BI at scale.</p>
  </section>
  <section class="abs week" style="left:963px;width:196px">
    <div class="week-label display">Week 6</div>
    <div class="week-name">Business outcomes +<br>AI-ready capability</div>
    <p class="week-text">Executive dashboards and priority reports, performance optimisation, hypercare and handover, AI readiness check and pilot plan (predictive analytics and/or secure enterprise LLM).</p>
  </section>

  <svg class="abs extra-band" width="1200" height="140" viewBox="0 0 1200 140" aria-hidden="true">
    <rect width="1200" height="140" fill="#17184a"/>
    <line x1="0" y1="1" x2="1200" y2="1" stroke="#fff" stroke-width="2"/>
    <polygon points="1120,2 1200,2 1200,140 1120,140 1140,71" fill="#17184a"/>
    <polygon points="890,2 1120,2 1140,71 1120,140 890,140 910,71" fill="#2b2878" stroke="#fff" stroke-width="2"/>
    <polygon points="660,2 890,2 910,71 890,140 660,140 680,71" fill="#2e3a9a" stroke="#fff" stroke-width="2"/>
    <polygon points="432,2 660,2 680,71 660,140 432,140 452,71" fill="#1479c4" stroke="#fff" stroke-width="2"/>
    <polygon points="188,2 432,2 452,71 432,140 188,140 208,71" fill="#2aaee6" stroke="#fff" stroke-width="2"/>
  </svg>

  <h2 class="abs display extra-title">Extra<span>Edge</span></h2>

  <section class="abs extra-item" style="left:222px">
    <div class="extra-name">“AI-ready data” guarantee</div>
    <p class="extra-text">Every priority dataset ships with validation rules, ownership, lineage, and freshness SLAs before it can power AI.</p>
  </section>
  <section class="abs extra-item" style="left:462px">
    <div class="extra-name">Cost-to-serve transparency</div>
    <p class="extra-text">Show business owners what each product/report costs to run and optimise it continuously.</p>
  </section>
  <section class="abs extra-item" style="left:693px">
    <div class="extra-name">Change-proof pipelines</div>
    <p class="extra-text">Data contracts + automated tests reduce breakages from upstream schema changes.</p>
  </section>
  <section class="abs extra-item" style="left:930px">
    <div class="extra-name">Governed self-serve</div>
    <p class="extra-text">Catalog + certified datasets so teams move faster without creating data chaos.</p>
  </section>

</main>
</body>
</html>
```